Business Promotion A1 Poster

I need an A1 poster for a lift in my building. It needs to promote BrightHarbour aa an employment expert for small business wanting to get their employment stuff right. We do on-site employment audits in Wellington for free.

We help small business manage the new 90 day trial period and help them design office/business policy manuals to avoid workplace problems.

The final design needs to convey expert and experience in employment. We use orange and grey as corporate colours. The company logo can be found on our website www.brightharbour.co.nz

Target Market(s)

Small business owners and managers

Industry/Entity Type

Small Business

Requirements
Nice to have
• colour information experts employment law in NZ

```html
<!DOCTYPE html>
<html lang="en">
<head>
<meta charset="utf-8">
<title>BrightHarbour – Our People, Your Potential</title>
<link rel="stylesheet" href="https://fonts.googleapis.com/css2?family=Arimo:wght@400;700&family=Open+Sans:wght@800&family=Oswald:wght@700&display=swap">
<style>
  :root {
    --white: #ffffff;
    --khaki: #dcd89a;
    --panel: #dedca6;
    --olive: #8c8c14;
    --olive-dark: #7a6a10;
    --orange: #f0961e;
    --grey: #8a8a8a;
    --room-dark: #4a3a28;
    --room-mid: #9a7e5c;
    --room-light: #d9c9ae;
    --floor: #efe9e0;
  }
  * { margin: 0; padding: 0; box-sizing: border-box; }
  html, body { width: 927px; height: 1200px; overflow: hidden; background: var(--white); }
  .poster {
    position: relative;
    width: 927px;
    height: 1200px;
    overflow: hidden;
    background: var(--white);
    font-family: "Arimo", Arial, sans-serif;
  }
  .boardroom-photo {
    position: absolute;
    left: 0; top: 0;
    width: 927px; height: 752px;
    background:
      linear-gradient(180deg, rgba(255,255,255,0) 0%, rgba(255,255,255,0) 66%, var(--floor) 84%, var(--white) 100%),
      radial-gradient(ellipse at 45% 28%, var(--room-light) 0%, var(--room-mid) 45%, var(--room-dark) 100%);
  }
  .tagline-band {
    position: absolute;
    left: 0; top: 507px;
    width: 927px; height: 100px;
    background: rgba(255,255,255,0.72);
  }
  .tagline {
    position: absolute;
    left: 46px; top: 22px;
    font-size: 33px;
    color: var(--olive);
    white-space: nowrap;
  }
  .tagline em { font-style: normal; color: var(--orange); }
  .headline {
    position: absolute;
    inset: 0;
    color: var(--white);
    text-shadow: 3px 3px 6px rgba(0,0,0,0.55);
    pointer-events: none;
  }
  .headline span {
    position: absolute;
    display: block;
    line-height: 1;
    white-space: nowrap;
  }
  .headline-our,
  .headline-potential {
    font-family: "Open Sans", Verdana, sans-serif;
    font-weight: 800;
  }
  .headline-our { left: 16px; top: 229px; font-size: 80px; letter-spacing: 1px; }
  .headline-people {
    left: 16px; top: 306px;
    font-family: "Oswald", "Arial Narrow", sans-serif;
    font-weight: 700;
    font-size: 115px;
    letter-spacing: 2px;
    color: var(--khaki);
  }
  .headline-potential { left: 24px; top: 405px; font-size: 98px; letter-spacing: 3px; }
  .contact-panel {
    position: absolute;
    left: 0; top: 752px;
    width: 528px; height: 448px;
    background: var(--panel);
  }
  .team-photo {
    position: absolute;
    left: 54px; top: 657px;
    width: 396px; height: 300px;
    border-radius: 46% 46% 30% 30% / 30% 30% 20% 20%;
    background: radial-gradient(ellipse at 50% 45%, #6e6a66 0%, #4a4644 55%, rgba(74,70,68,0.6) 100%);
  }
  .service-line {
    position: absolute;
    left: 30px; top: 998px;
    font-size: 23px;
    color: var(--olive-dark);
    white-space: nowrap;
  }
  .address {
    position: absolute;
    left: 30px; top: 1034px;
    font-size: 22px;
    line-height: 28px;
    color: var(--olive);
  }
  .phone-row {
    position: absolute;
    left: 22px; top: 1158px;
    font-size: 17px;
    color: var(--olive-dark);
    white-space: nowrap;
  }
  .phone-row .arrow { color: var(--white); margin: 0 4px 0 2px; }
  .phone-row strong { font-size: 21px; color: var(--orange); font-weight: 700; }
  .phone-row .fax { margin-left: 44px; }
  .brand {
    position: absolute;
    left: 597px; top: 930px;
    display: flex;
    align-items: center;
    gap: 14px;
  }
  .brand-name { font-size: 36px; color: var(--grey); }
  .brand-square { width: 52px; height: 52px; background: var(--orange); }
  .website {
    position: absolute;
    left: 564px; top: 1104px;
    font-size: 26px;
    color: var(--olive);
  }
</style>
</head>
<body>
  <main class="poster">
    <div class="boardroom-photo" role="img" aria-label="Photo of a bright modern boardroom with a long wooden table, black chairs, chandeliers and city windows"></div>

    <div class="tagline-band">
      <p class="tagline"><em>Employment</em> Experts for <em>Small Business</em>......</p>
    </div>

    <h1 class="headline">
      <span class="headline-our">Our</span>
      <span class="headline-people">People</span>
      <span class="headline-potential">Your Potential</span>
    </h1>

    <section class="contact-panel" aria-label="Contact details"></section>
    <div class="team-photo" role="img" aria-label="Photo of a diverse group of business professionals standing together"></div>

    <p class="service-line">Free audits, 90-day trials, policy manuals</p>
    <p class="address">Address : Level 4, 18 Harbour Lane,<br>Wellington, 6011</p>
    <p class="phone-row">Please call<span class="arrow">&gt;</span><strong>04 555 0142</strong><span class="fax">Fax<span class="arrow">&gt;</span><strong>04 555 0143</strong></span></p>

    <div class="brand">
      <span class="brand-name">BrightHarbour</span>
      <span class="brand-square" aria-hidden="true"></span>
    </div>
    <p class="website">www.brightharbour.co.nz</p>
  </main>
</body>
</html>
```